Marlow & Tate
Business card and stationery design for a management consulting firm  - Consulting
Simple
Benedikt Owen Dolsquin
Lead Consultant
Njegoševa 47 11000 Belgrade
benedikt.owen@marlowtate-example.com
www.marlowtate-example.com
Keep the design clean. "Scandinavian design approach". Address line on business card is preferred not to be included, although if designer finds it to complete the holistic 'picture' of the card, then he/she may use it. Font selection for the rest of the text is up to the designer. Although please note that the font has to be in balance with the logo. Business cards are to be printed on black paper / metal. If printed on paper, the logo part will be with relief printing.
This is designers choice to be creative
dolsquin dolsquin
Tip to designers: Try not to use the monogram "MT" with "Marlow and Tate" on the same side. Printing techniques that will be used are: Embossing / Debossing, Thermography. Keep it clean. Less is more.

```html
<!DOCTYPE html>
<html lang="en">
<head>
<meta charset="utf-8">
<title>Marlow &amp; Tate — Business Card</title>
<link rel="stylesheet" href="https://fonts.googleapis.com/css2?family=Raleway:wght@300;400&display=swap">
<style>
  :root {
    --backdrop: #3b2225;
    --card: #141414;
    --card-edge: #1f1f1f;
    --ink: #e9e9e9;
    --ink-soft: #a9a9a9;
    --rule: #d8d8d8;
    --rule-soft: #6f6f6f;
  }
  * { margin: 0; padding: 0; box-sizing: border-box; }
  html, body {
    width: 1200px; height: 672px; overflow: hidden;
    background: var(--backdrop);
    font-family: "Raleway", sans-serif;
    color: var(--ink);
  }
  .stage {
    position: relative; width: 1200px; height: 672px;
    display: flex; align-items: center; justify-content: center; gap: 60px;
  }
  .card {
    position: relative; width: 520px; height: 336px;
    background: var(--card);
    border: 1px solid var(--card-edge);
    overflow: hidden;
  }
  .card-lines { position: absolute; inset: 0; width: 100%; height: 100%; }
  .brand-name {
    position: absolute;
    font-weight: 300; letter-spacing: 0.06em;
    color: var(--ink);
    white-space: nowrap;
  }
  .card-front .brand-name { top: 46px; right: 44px; font-size: 26px; }
  .card-back .brand-name {
    top: 140px; left: 0; right: 0; text-align: center; font-size: 36px;
  }
  .person {
    position: absolute; left: 40px; top: 150px;
  }
  .person-name { font-size: 17px; font-weight: 300; letter-spacing: 0.02em; }
  .person-rule { width: 230px; height: 1px; background: var(--rule-soft); margin: 6px 0 5px; }
  .person-role { font-size: 10px; font-weight: 300; color: var(--ink-soft); letter-spacing: 0.04em; }
  .contact {
    position: absolute; right: 40px; bottom: 58px;
    text-align: right; font-size: 10px; font-weight: 300; line-height: 1.6;
    color: var(--ink-soft); letter-spacing: 0.03em;
  }
  .web {
    position: absolute; right: 40px; bottom: 62px;
    font-size: 10px; font-weight: 300; color: var(--ink-soft); letter-spacing: 0.05em;
  }
</style>
</head>
<body>
  <main class="stage">
    <article class="card card-front">
      <svg class="card-lines" viewBox="0 0 520 336" aria-hidden="true">
        <line x1="0" y1="318" x2="520" y2="296" stroke="var(--rule)" stroke-width="1.4"/>
      </svg>
      <div class="brand-name">Marlow and Tate</div>
      <div class="person">
        <div class="person-name">Benedikt Owen Dolsquin</div>
        <div class="person-rule"></div>
        <div class="person-role">Lead Consultant</div>
      </div>
      <div class="contact">
        <div>Njegoševa 47 11000 Belgrade</div>
        <div>Cell: +381 60 1 555 014</div>
        <div>Email: benedikt.owen@marlowtate-example.com</div>
      </div>
    </article>

    <article class="card card-back">
      <svg class="card-lines" viewBox="0 0 520 336" aria-hidden="true">
        <line x1="0" y1="298" x2="520" y2="270" stroke="var(--rule)" stroke-width="1.4"/>
        <line x1="0" y1="312" x2="520" y2="284" stroke="var(--rule-soft)" stroke-width="1"/>
      </svg>
      <div class="brand-name">Marlow and Tate</div>
      <div class="web">www.marlowtate-example.com</div>
    </article>
  </main>
</body>
</html>
```